Design a corporate looking website for Harbourline Funding

Need design only WordPress mock up for Harbourline Funding who provides short term finance solutions to other businesses. We need a corporate looking website that depicts a trustworthy, Dynamic fast acting company.
Visit http://k7.pagelantern-demo.net/ for current mock up We need something like e this but not the same with a design that depicts corporate with more colour and images, needs to install trust and fast action. Please feel free to change the layout as I am not wedded to current design but am happy with what on the landing page.

Target Market(s)

Small to medium sized Businesses

Industry/Entity Type

Finance

Number of Pages Required

1 page

Font styles to use
Sans Serif

Requirements
Must have
• Design Landing pages in WordPress
• Visit http://k7.pagelantern-demo.net/ for current mock up need Layout like this but with a design that depicts corporate with more colour and images, needs to install trust and fast action. Please feel free to change the layout as I am not happy with current design but am wedded to what on the landing page.
Should not have
• any copyright material on it.

```html
<!DOCTYPE html>
<html lang="en">
<head>
<meta charset="utf-8">
<title>Harbourline Funding</title>
<link href="https://fonts.googleapis.com/css2?family=Roboto:wght@300;400;500;700&display=swap" rel="stylesheet">
<style>
:root{
  --blue:#4a87c2;
  --ink:#3d3d3d;
  --muted:#8d8d8d;
  --light:#f7f7f7;
  --dark:#2c2e33;
  --lime:#c5d92d;
  --green:#8bc34a;
  --vip:#5b8cc8;
  --teal:#139483;
  --white:#fff;
}
*{box-sizing:border-box;margin:0;padding:0}
html,body{width:1200px;height:1200px;overflow:hidden;background:#fff;font-family:'Roboto',sans-serif;color:var(--ink)}
.page{position:absolute;left:380px;top:0;width:442px;height:1200px;background:var(--light);overflow:hidden}
.abs{position:absolute}
.band{position:absolute;left:0;width:442px}
.blue{background:var(--blue)}
.tiny{font-size:3.6px;line-height:5.4px;color:var(--muted)}
.tiny.light{color:#dbe7f3}
/* header */
.site-header{top:0;height:30px;background:#fff}
.brand{left:100px;top:8px;display:flex;align-items:center;gap:3px;font-size:6px;font-weight:700;color:#1f3d7a;letter-spacing:.1px}
.brand .mark{width:7px;height:7px;border-radius:50%;background:var(--blue)}
.nav{left:186px;top:13px;display:flex;gap:9px;font-size:3.4px;color:#555}
.nav .active{color:var(--blue)}
.plus{left:327px;top:23px;width:16px;height:16px;border-radius:50%;background:#3a3d44;color:#fff;font-size:10px;line-height:16px;text-align:center;z-index:3}
/* hero */
.hero{top:30px;height:220px}
.hero h1{position:absolute;left:86px;top:70px;font-weight:300;font-size:19px;color:#2f3a48}
.hero h2{position:absolute;left:86px;top:96px;font-weight:300;font-size:10px;color:#2f4f73}
.btn-dark{background:#24272c;color:#fff;font-size:3.2px;border-radius:5px;text-align:center;line-height:8px;height:8px}
.btn-line{border:.6px solid #fff;color:#fff;font-size:3.2px;border-radius:5px;text-align:center;line-height:7px;height:8px}
.art{background:linear-gradient(160deg,#6fa1d2,#3f78b3)}
/* features */
.features{top:250px;height:108px;background:var(--light)}
.feature{position:absolute;width:90px;text-align:center}
.feature .icon{width:26px;height:26px;border-radius:50%;border:.6px solid #e3e3e3;background:#fff;margin:0 auto;display:flex;align-items:center;justify-content:center}
.feature h3{font-size:6.5px;font-weight:400;margin:8px 0 2px}
.notch{left:215px;top:357px;width:0;height:0;border-left:6px solid transparent;border-right:6px solid transparent;border-top:6px solid var(--light);z-index:2}
/* flow */
.flow{top:358px;height:163px}
.flow h2{position:absolute;left:224px;top:25px;font-weight:300;font-size:10px;line-height:11px;color:#fff}
.checks{left:237px;top:72px;list-style:none}
.checks li{font-size:3.2px;color:#fff;height:9.4px;position:relative}
.checks li::before{content:"";position:absolute;left:-8px;top:0;width:3px;height:1.6px;border-left:.6px solid #fff;border-bottom:.6px solid #fff;transform:rotate(-45deg)}
/* plans */
.plans{top:521px;height:216px;background:var(--light)}
.section-title{font-weight:300;font-size:10px;color:#333}
.plan{position:absolute;width:67px;top:68px;height:120px;background:#fff;text-align:center}
.plan .head{height:23px;color:#fff;font-size:6px;font-weight:700;padding-top:6px}
.plan .head small{display:block;font-size:2.4px;font-weight:400;opacity:.8}
.plan .rate{height:26px;color:#fff;font-size:12px;font-weight:300;line-height:26px}
.plan .body{padding:9px 8px;height:46px}
.plan .foot{height:25px;background:#f0f0f0;padding-top:7px}
.plan .go{width:52px;height:10px;margin:0 auto;border-radius:5px;color:#fff;font-size:3px;line-height:10px}
.plan.vip{top:61px;height:133px;box-shadow:0 1px 4px rgba(0,0,0,.15);z-index:2}
.plan.vip .head{height:30px;padding-top:4px}
.plan.vip .foot{height:31px;background:#fff;padding-top:11px}
/* answers */
.answers{top:737px;height:193px}
.answers h2{position:absolute;left:86px;top:31px;font-weight:300;font-size:10px;color:#2f3a48}
.faq{left:86px;top:73px;width:131px}
.faq .item{font-size:3.6px;color:#2f4f73;border-bottom:.5px solid #7fa7d3;height:13.5px;line-height:9px;position:relative}
.faq .item::after{content:"";position:absolute;right:1px;top:3px;width:1.8px;height:1.8px;border-right:.5px solid #2f4f73;border-bottom:.5px solid #2f4f73;transform:rotate(45deg)}
.faq .item.open{color:var(--green);border:none;height:9px}
.faq .answer{padding-bottom:4px;border-bottom:.5px solid #7fa7d3;margin-bottom:4px}
/* payments */
.payments{top:930px;height:102px;background:#fff}
.pay{position:absolute;top:62px;font-size:9px;font-weight:700;color:#26426e;transform:translateX(-50%);white-space:nowrap}
.dots{left:336px;top:46px;display:flex;gap:2.5px}
.dots i{width:2px;height:2px;border-radius:50%;background:#ccc}
.dots i.on{background:var(--lime)}
/* footer */
.site-footer{top:1032px;height:138px;background:var(--light)}
.field{font-size:3.4px;color:#333;border-bottom:.6px solid #ccc;width:86px;height:10px}
.social{left:86px;top:97px;display:flex;gap:2px}
.social i{width:7px;height:7px;border-radius:50%}
.bottom{top:1170px;height:30px;background:var(--dark)}
.up{left:338px;top:1160px;width:16px;height:16px;border-radius:50%;background:var(--dark);z-index:3}
</style>
</head>
<body>
<div class="page">

  <header class="band site-header">
    <div class="abs" style="left:86px;top:12px;width:4px">
      <div style="height:.7px;background:#444;margin-bottom:1px"></div>
      <div style="height:.7px;background:#444;margin-bottom:1px"></div>
      <div style="height:.7px;background:#444"></div>
    </div>
    <div class="abs brand"><span class="mark"></span>HARBOURLINE FUNDING</div>
    <nav class="abs nav">
      <span class="active">Home</span><span>Pages</span><span>Investment</span><span>News</span><span>Calculator</span><span>Contacts</span>
    </nav>
    <div class="abs" style="left:354px;top:13px;font-size:5px;line-height:2px;color:#444">·<br>·<br>·</div>
  </header>
  <div class="abs plus">+</div>

  <section class="band hero blue">
    <h1>Hello World!</h1>
    <h2>Welcome to Good Investment</h2>
    <p class="abs tiny" style="left:86px;top:113px;width:130px;color:#2f4f73">Short term finance for growing firms, fast decisions and clear terms for every business partner.</p>
    <div class="abs btn-dark" style="left:86px;top:136px;width:33px">Learn More ›</div>
    <div class="abs art" role="img" aria-label="Illustration of a hand holding a plant growing coins and banknotes, with floating money" style="left:228px;top:22px;width:142px;height:198px;border-radius:4px"></div>
  </section>

  <section class="band features">
    <div class="feature" style="left:85px;top:22px">
      <div class="icon"><svg width="11" height="10" viewBox="0 0 11 10"><rect x="1" y="4" width="2" height="6" fill="#4a87c2"/><rect x="4.5" y="1" width="2" height="9" fill="#4a87c2"/><rect x="8" y="3" width="2" height="7" fill="#4a87c2"/></svg></div>
      <h3>Investment Solutions</h3>
      <p class="tiny">Flexible funding built around your cash cycle, with quick approval and simple repayment plans.</p>
    </div>
    <div class="feature" style="left:176px;top:22px">
      <div class="icon" style="background:#fbeee0;border-color:#f3e0cc"><svg width="12" height="10" viewBox="0 0 12 10"><rect x="1" y="6" width="1.6" height="4" fill="#4a87c2"/><rect x="4" y="4" width="1.6" height="6" fill="#4a87c2"/><rect x="7" y="5" width="1.6" height="5" fill="#4a87c2"/><rect x="10" y="2" width="1.6" height="8" fill="#4a87c2"/><polyline points="1,4 4,2 7,3 11,0" fill="none" stroke="#4a87c2" stroke-width=".8"/></svg></div>
      <h3 style="color:var(--green)">Strategy Design</h3>
      <p class="tiny">Plans shaped with your team to keep growth steady, costs low and every step easy to follow.</p>
    </div>
    <div class="feature" style="left:268px;top:22px">
      <div class="icon"><svg width="11" height="9" viewBox="0 0 11 9"><rect x=".5" y=".5" width="10" height="8" rx="1" fill="none" stroke="#555" stroke-width=".8"/><circle cx="5.5" cy="4.5" r="2" fill="none" stroke="#555" stroke-width=".8"/></svg></div>
      <h3>Financial Integration</h3>
      <p class="tiny">Funding that links with your accounts so money arrives on time and reporting stays clear.</p>
    </div>
  </section>
  <div class="abs notch"></div>

  <section class="band flow blue">
    <div class="abs art" role="img" aria-label="Illustration of a businessman standing on a coin pillar among clouds" style="left:64px;top:22px;width:152px;height:141px;border-radius:4px"></div>
    <h2>Maintain financial flow<br>and invest wisely</h2>
    <p class="abs tiny light" style="left:224px;top:56px;width:130px;color:#fff">Keep cash moving with short term loans that arrive fast, so your business never waits on payments.</p>
    <ul class="abs checks">
      <li>Funds within two days</li>
      <li>No hidden fees</li>
      <li>Clear terms</li>
      <li>Fixed monthly rates</li>
      <li>Local support team</li>
    </ul>
    <div class="abs btn-dark" style="left:224px;top:126px;width:34px">Learn More ›</div>
    <div class="abs btn-line" style="left:266px;top:126px;width:34px">Contact Us ›</div>
  </section>

  <section class="band plans">
    <h2 class="abs section-title" style="left:0;width:442px;top:21px;text-align:center">Investment Plans</h2>
    <p class="abs tiny" style="left:131px;width:180px;top:40px;text-align:center">Choose a plan that fits your needs, each one with quick payout and plain pricing for growing firms.</p>

    <div class="plan" style="left:86px">
      <div class="head" style="background:var(--lime)">Standart<small>15 calendar days</small></div>
      <div class="rate" style="background:#cfe03a">0.5%</div>
      <p class="body tiny">Short term support for small firms with steady daily sales and low risk.</p>
      <div class="foot"><div class="go" style="background:var(--lime)">Invest now!</div></div>
    </div>
    <div class="plan" style="left:153px">
      <div class="head" style="background:var(--green)">Professional<small>30 calendar days</small></div>
      <div class="rate" style="background:#97cb55">0.8%</div>
      <p class="body tiny">Monthly funding for teams that need stock, staff or fresh equipment fast.</p>
      <div class="foot"><div class="go" style="background:var(--green)">Invest now!</div></div>
    </div>
    <div class="plan vip" style="left:220px">
      <div class="head" style="background:var(--vip)">VIP Partner<small>60 calendar days</small></div>
      <div class="rate" style="background:#6a98cf">1.2%</div>
      <p class="body tiny">Priority access to larger sums with a named adviser and review support.</p>
      <div class="foot"><div class="go" style="background:var(--vip)">Invest now!</div></div>
    </div>
    <div class="plan" style="left:288px">
      <div class="head" style="background:var(--teal)">Business<small>90 calendar days</small></div>
      <div class="rate" style="background:#1fa08e">1.0%</div>
      <p class="body tiny">Longer term capital for firms ready to expand into new regions soon.</p>
      <div class="foot"><div class="go" style="background:var(--teal)">Invest now!</div></div>
    </div>
  </section>

  <section class="band answers blue">
    <h2>Quick Answers</h2>
    <p class="abs tiny" style="left:86px;top:50px;width:130px;color:#fff">Common questions about our loans, how fast funds arrive and what you need to apply.</p>
    <div class="abs faq">
      <div class="item">How fast can I get funds</div>
      <div class="item">What documents are needed</div>
      <div class="item open">Who can apply</div>
      <p class="answer tiny" style="color:#fff">Any registered firm trading for six months or more can apply online in minutes and get a decision within one working day.</p>
      <div class="item">Are there early repayment fees</div>
      <div class="item" style="border:none">Can I extend my term</div>
    </div>
    <div class="abs art" role="img" aria-label="Illustration of a puzzled businessman holding his head with question marks above" style="left:252px;top:19px;width:96px;height:174px;border-radius:4px"></div>
  </section>

  <section class="band payments">
    <h2 class="abs section-title" style="left:86px;top:22px">Payment Systems</h2>
    <p class="abs tiny" style="left:86px;top:40px;width:130px">Pay and receive funds through the services your business already uses.</p>
    <div class="abs dots"><i></i><i class="on"></i><i></i><i></i><i></i></div>
    <span class="pay" style="left:118px">Tallowpay</span>
    <span class="pay" style="left:186px">Coinmere</span>
    <span class="pay" style="left:256px">Zolvix</span>
    <span class="pay" style="left:324px">Parrowly</span>
  </section>

  <footer class="band site-footer">
    <div class="abs brand" style="left:86px;top:21px"><span class="mark"></span>HARBOURLINE FUNDING</div>
    <p class="abs tiny" style="left:86px;top:43px;width:86px;color:#555">Harbourline Funding offers fast short term finance to small and medium firms, with plain terms and real people ready to help. <span style="color:var(--green)">Read More</span></p>
    <div class="abs social">
      <i style="background:#3b5b9a"></i><i style="background:#3ba0d8"></i><i style="background:#d84a38"></i><i style="background:#c8232c"></i><i style="background:#6b4f3a"></i><i style="background:#4cae4c"></i><i style="background:#999"></i><i style="background:#2b6dad"></i><i style="background:#e24a6e"></i>
    </div>

    <p class="abs tiny" style="left:178px;top:45px;color:#555">◷ 07 May 2015</p>
    <p class="abs tiny" style="left:184px;top:51px;width:80px">New loan plans for retail firms now open for online requests.</p>
    <div class="abs" style="left:178px;top:67px;width:86px;height:.6px;background:#ccc"></div>
    <p class="abs tiny" style="left:184px;top:76px;color:var(--green)">Spring rates update</p>
    <div class="abs" style="left:178px;top:84px;width:86px;height:.6px;background:#ccc"></div>
    <p class="abs tiny" style="left:178px;top:90px;color:#555">◷ 03 December 2014</p>
    <p class="abs tiny" style="left:184px;top:96px;width:80px">Our team grows with new advisers across the region.</p>

    <p class="abs tiny" style="left:270px;top:45px;width:86px">Sign up for our newsletter to get the latest updates and offers.</p>
    <div class="abs field" style="left:270px;top:60px">Full Name</div>
    <div class="abs field" style="left:270px;top:77px">Email Address</div>
    <div class="abs" style="left:270px;top:97px;width:32px;height:8px;border-radius:4px;background:var(--green);color:#fff;font-size:2.8px;line-height:8px;text-align:center">Subscribe Now</div>
  </footer>
  <div class="abs up"><svg width="16" height="16" viewBox="0 0 16 16"><polyline points="5.5,9 8,6.5 10.5,9" fill="none" stroke="#fff" stroke-width="1"/></svg></div>
  <div class="band bottom"></div>

</div>
</body>
</html>
```